Colour consulting and Interior design company needs a squarespace web design

we need a website design for squarespace for a Melbourne based company called 'Brightwell Rooms' which incorporates the existing logo. The company primarily provides colour consulting for residential and commercial as well as interior design services. Schemes are personalised for each client. I would like the design to have some colour and use the colour palette provided but it is not is not totally exclusive. The final design should indicate character, playfulness, functionality , harmony and joy. I like the blue/green core colour with the white and would like that to be incorporated.
as per image provided below - double sided
4 page
- space for some images but not too many.
- Page for booking consultation
- real images of houses

```html
<!DOCTYPE html>
<html lang="en">
<head>
<meta charset="utf-8">
<title>Brightwell Rooms</title>
<link href="https://fonts.googleapis.com/css2?family=Quattrocento:wght@400;700&family=Open+Sans:wght@400;600;700&family=Montserrat:wght@400;600;700&display=swap" rel="stylesheet">
<style>
:root{
  --ink:#2b2b2b;
  --text:#555;
  --muted:#8a8a8a;
  --blue:#3a8fd0;
  --teal:#a9ded5;
  --teal-soft:#cfebe6;
  --footer-bg:#f7f7f7;
  --rule:#e3e3e3;
  --button-line:#9ed9cd;
}
*{margin:0;padding:0;box-sizing:border-box}
html,body{width:1200px;height:2651px;overflow:hidden;background:#fff}
body{position:relative;font-family:"Open Sans",sans-serif;color:var(--text)}
.abs{position:absolute}

.site-header{position:absolute;left:0;top:0;width:1200px;height:57px;background:#fff}
.brand{position:absolute;left:94px;top:17px;display:flex;align-items:center;gap:8px;font-family:"Open Sans",sans-serif;font-weight:700;font-size:15px;color:#2d5f86}
.brand-mark{width:18px;height:18px;background:#2d5f86}
.main-nav{position:absolute;top:22px;left:0;font-size:10px;font-weight:700;letter-spacing:1px;color:var(--ink)}
.main-nav a{position:absolute;white-space:nowrap;color:inherit;text-decoration:none}
.nav-contact{position:absolute;left:1050px;top:0;width:150px;height:57px;background:var(--blue);color:#fff;font-size:10px;font-weight:700;letter-spacing:1px;display:flex;align-items:center;justify-content:center}

.hero{position:absolute;left:0;top:57px;width:1200px;height:614px;background:linear-gradient(100deg,#e7e3df 0%,#f3f1ee 35%,#ece9e5 60%,#d9d4cf 100%)}
.hero-frame{position:absolute;left:279px;top:269px}
.hero-title{position:absolute;left:0;top:292px;width:1200px;text-align:center;font-family:"Quattrocento",serif;font-size:62px;color:#2a2a2a;line-height:1}

.section-title{font-family:"Quattrocento",serif;font-weight:400;color:var(--ink);font-size:38px;line-height:1}
.about-title{left:0;top:765px;width:1200px;text-align:center}
.about-sub{left:0;top:810px;width:1200px;text-align:center;font-family:"Quattrocento",serif;font-size:17px;color:var(--ink)}
.rule{height:1px;width:74px;background:#777}
.about-text{left:360px;top:875px;width:481px;text-align:center;font-size:11px;line-height:17.5px;color:#666}
.about-text p+p{margin-top:17px}

.photo{position:absolute}
.block-teal{background:var(--teal)}
.block-teal-soft{background:var(--teal-soft)}
.feature-text{font-size:11px;line-height:17px;color:#666}
.btn-outline{position:absolute;width:147px;height:30px;border:1.5px solid var(--button-line);display:flex;align-items:center;justify-content:center;font-size:8px;font-weight:700;letter-spacing:1.5px;color:var(--ink)}

.site-footer{position:absolute;left:0;top:2327px;width:1200px;height:324px;background:var(--footer-bg);border-top:1px solid #ececec;font-family:"Montserrat",sans-serif}
.footer-head{position:absolute;font-size:12px;font-weight:700;letter-spacing:.5px;color:var(--ink)}
.footer-line{position:absolute;font-size:10px;color:var(--muted);line-height:14px}
.footer-link{color:#5a87ad}
.footer-rule{position:absolute;left:235px;top:263px;width:732px;height:1px;background:var(--rule)}
.copyright{position:absolute;left:235px;top:285px;font-size:9px;color:#aaa}
.copyright b{color:#777;font-weight:600}
.social{position:absolute;left:888px;top:284px;display:flex;gap:11px}
.social span{width:12px;height:12px;border-radius:50%;background:#8a8a8a;display:block}
</style>
</head>
<body>

<header class="site-header">
  <div class="brand"><span class="brand-mark"></span>Brightwell Rooms</div>
  <nav class="main-nav">
    <a style="left:426px">HOME</a>
    <a style="left:486px">MARKET GUIDE</a>
    <a style="left:588px">BROWSE BY PROJECT</a>
    <a style="left:716px">BROWSE BY ROOM</a>
    <a style="left:834px">SERVICES</a>
    <a style="left:910px">INSPIRED</a>
    <a style="left:986px">ABOUT</a>
  </nav>
  <div class="nav-contact">CONTACT US</div>
</header>

<section class="hero" role="img" aria-label="Bright white bedroom with a woman stretching happily on an unmade bed"></section>
<svg class="hero-frame" width="624" height="132" viewBox="0 0 624 132" aria-hidden="true">
  <path d="M100 2.5H2.5V129.5H100" fill="none" stroke="#333" stroke-width="5"/>
  <path d="M516 2.5H621.5V129.5H516" fill="none" stroke="#333" stroke-width="5"/>
</svg>
<h1 class="hero-title">The art of living</h1>

<h2 class="abs section-title about-title">About us</h2>
<p class="abs about-sub">Lorem ipsum dolor sit amet, consectetur adipiscing</p>
<div class="abs rule" style="left:563px;top:853px"></div>
<div class="abs about-text">
  <p>Lorem ipsum dolor sit amet, consectetur adipiscing elit, sed do eiusmod tempor incididunt ut labore et dolore magna aliqua. Ut enim ad minim veniam, quis nostrud exercitation ullamco exercitatio commodo laboris nisi ut aliquip ex ea commodo consequat.</p>
  <p>Sed ut perspiciatis unde omnis iste natus error sit voluptatem accusantium doloremque laudantium, totam rem aperiam, eaque ipsa quae ab illo inventore veritatis et quasi architecto beatae vitae dicta sunt explicabo. Nemo enim ipsam voluptatem quia voluptas sit aspernatur aut odit aut fugit, sed quia consequuntur magni dolores eos qui ratione voluptatem sequi nesciunt.</p>
</div>

<div class="abs block-teal" style="left:0;top:1131px;width:465px;height:498px"></div>
<div class="photo" style="left:81px;top:1212px;width:534px;height:338px;background:linear-gradient(180deg,#cfc6b8 0%,#b7ab98 58%,#9a6a3c 75%,#b47a40 100%)" role="img" aria-label="Woven rattan armchair with a lime cushion beside potted plants on a wooden floor"></div>
<h2 class="abs section-title" style="left:777px;top:1278px">Residential</h2>
<div class="abs rule" style="left:777px;top:1341px"></div>
<p class="abs feature-text" style="left:777px;top:1363px;width:322px">Lorem ipsum dolor sit amet, consectetur adipiscing elit, sed do eiusmod tempor incididunt ut labore et dolore magna aliqua. Ut enim ad minim veniam, quis nostrud exercitation ullamco.</p>
<div class="btn-outline" style="left:777px;top:1445px">LEARN MORE</div>

<div class="abs block-teal-soft" style="left:484px;top:1707px;width:481px;height:449px"></div>
<div class="photo" style="left:562px;top:1785px;width:466px;height:422px;background:linear-gradient(180deg,#8d9aa3 0%,#c7d0d4 45%,#e4e6e6 70%,#cfd1d2 100%)" role="img" aria-label="Glass-walled office lobby with black lounge chairs and planters"></div>
<h2 class="abs section-title" style="left:235px;top:1807px">Commercial</h2>
<div class="abs rule" style="left:235px;top:1873px"></div>
<p class="abs feature-text" style="left:235px;top:1900px;width:185px">Lorem ipsum dolor sit amet, consectetur adipiscing elit, sed do eiusmod tempor incididunt ut labore et dolore magna aliqua. Ut enim ad minim.</p>
<div class="btn-outline" style="left:235px;top:1993px">LEARN MORE</div>

<footer class="site-footer">
  <div class="brand" style="left:235px;top:74px">
    <span class="brand-mark"></span>Brightwell Rooms
  </div>
  <div class="footer-head" style="left:546px;top:74px">CONTACT US</div>
  <div class="footer-line" style="left:546px;top:112px;width:200px">14 Laurel Lane, Fitzroy North,<br>VIC 3068, Australia</div>
  <div class="footer-line" style="left:546px;top:168px">P: 03 - 555 - 0142</div>
  <div class="footer-line" style="left:546px;top:193px">E: <span class="footer-link">hello@brightwellrooms.example</span></div>
  <div class="footer-head" style="left:776px;top:74px">LEARN MORE</div>
  <div class="footer-line" style="left:776px;top:112px">Lorem ipsum</div>
  <div class="footer-line" style="left:776px;top:136px">Dolor set amet</div>
  <div class="footer-line" style="left:776px;top:159px">Adipiscing</div>
  <div class="footer-line" style="left:776px;top:182px">Set amet lorem</div>
  <div class="footer-rule"></div>
  <div class="copyright">© 2018 <b>Brightwell Rooms</b> All Rights Reserved</div>
  <div class="social" aria-label="Social links"><span></span><span></span><span></span><span></span></div>
</footer>

</body>
</html>
```